Veltrano Energy Business Card Design

website: www.veltranoenergy.example
Project: Business Card Design for Veltrano Energy
Name: Dorian Kettle
Title: Founder / Operations Strategist
Visual Identity & Logo:
Logo File: VEL-Logo-FullGradient-Final.png (Attached).
Color Palette: The brand relies on a distinctive Cyan (Blue) to Lime Green gradient.
Background Preference: We want a Dark Mode aesthetic (Deep Matte Black, Charcoal, or Dark Slate) to make the neon gradient of the logo pop. This feels more "tech/industrial" than a standard white card.
Design Aesthetic (The "Ops" Vibe):
Concept: "Grid & Infrastructure." We are a solar rental company, focusing on logistics and access.
Typography: White, bold sans-serif text for contact info. High contrast against the dark background.
Accents: Use the Cyan or Lime Green from the logo for thin divider lines or edge painting.
Avoid: No orange/gold (clashes with logo). No cartoon leaves.
Layout Requirements:
Front: Large, centered logo. Maybe a subtle UV gloss spot varnish over the logo icon.
Back: Name, Title, Contact Info.
Texture: Matte finish cardstock with gloss elements.
sample mock up of information on card: https://brivomarkco-my.filehost.example/:i:/g/personal/dorian_kettle_veltranoenergy_example/AbCdEfGhIjKlMnOpQrStUvWxYz012345678?e=Xy12Ab
Logo: https://brivomarkco.filehost.example/:i:/s/VeltranoEnergy/ZyXwVuTsRqPoNmLkJiHgFeDcBa9876543210?e=Pq34Cd

```html
<!DOCTYPE html>
<html lang="en">
<head>
<meta charset="utf-8">
<title>Veltrano Energy – Business Card</title>
<link href="https://fonts.googleapis.com/css2?family=Poppins:wght@300;400;600;700&display=swap" rel="stylesheet">
<style>
  :root {
    --canvas: #7d7d7d;
    --card-dark: #28282c;
    --card-mid: #313136;
    --cyan: #12b9d6;
    --teal: #16c9c3;
    --lime: #9fc83a;
    --white: #ffffff;
    --soft-white: #f1f1f1;
    --flag-frame: #d9d9d9;
  }
  * { margin: 0; padding: 0; box-sizing: border-box; }
  html, body { width: 872px; height: 1200px; overflow: hidden; }
  body {
    position: relative;
    background: var(--canvas);
    font-family: "Poppins", sans-serif;
    color: var(--white);
  }
  .card {
    position: absolute;
    left: 56px;
    width: 761px;
    height: 435px;
    background: linear-gradient(135deg, var(--card-mid) 0%, var(--card-dark) 60%, #2b2b2f 100%);
    box-shadow: 0 8px 18px rgba(0,0,0,0.28);
    overflow: hidden;
  }
  .card--front { top: 126px; }
  .card--back { top: 601px; }

  /* Brand name with plain square marker */
  .brand {
    position: absolute;
    display: flex;
    align-items: center;
    white-space: nowrap;
  }
  .brand__square { background: var(--teal); flex: none; }
  .brand__name {
    font-weight: 600;
    color: var(--white);
    line-height: 1;
  }
  .card--front .brand {
    left: 50%; top: 50%;
    transform: translate(-50%, -50%);
    gap: 22px;
  }
  .card--front .brand__square { width: 58px; height: 58px; }
  .card--front .brand__name { font-size: 54px; }

  .card--back .brand { left: 59px; top: 134px; gap: 12px; }
  .card--back .brand__square { width: 28px; height: 28px; }
  .card--back .brand__name { font-size: 23px; }

  .offices { position: absolute; left: 58px; top: 250px; }
  .offices__label { font-size: 13px; font-weight: 300; color: var(--soft-white); }
  .offices__flags { display: flex; gap: 4px; margin-top: 2px; }
  .offices__flag { width: 29px; height: 29px; border: 1px solid var(--flag-frame); }
  .offices__flag--a { background: linear-gradient(180deg, #3a4fa0 0 45%, #d84a4a 45% 100%); }
  .offices__flag--b { background: linear-gradient(90deg, #d43a3a 0 28%, #f4f4f4 28% 72%, #d43a3a 72% 100%); }
  .offices__flag--c { background: linear-gradient(180deg, #2c3f8a 0 40%, #f4f4f4 40% 60%, #2c3f8a 60% 100%); }

  .divider {
    position: absolute;
    left: 340px; top: 89px;
    width: 2px; height: 200px;
    background: var(--teal);
    opacity: 0.85;
  }

  .person { position: absolute; left: 368px; top: 83px; }
  .person__name { font-size: 32px; font-weight: 700; line-height: 1.1; letter-spacing: -0.3px; }
  .person__title { font-size: 12px; font-weight: 600; margin-left: 4px; }

  .contact { position: absolute; left: 378px; }
  .contact--address { top: 159px; }
  .contact--web { top: 262px; }
  .contact__icon { position: absolute; left: 0; top: 2px; }
  .contact__text {
    margin-left: 43px;
    font-size: 18px;
    font-weight: 400;
    line-height: 24.3px;
    color: var(--soft-white);
  }

  .tagline {
    position: absolute;
    left: 0; top: 337px;
    width: 761px; height: 42px;
    background: linear-gradient(90deg, var(--teal) 0%, #3aa88c 50%, var(--lime) 100%);
    display: flex; align-items: center; justify-content: center;
    font-size: 20px; font-weight: 300;
  }
</style>
</head>
<body>

  <section class="card card--front">
    <div class="brand">
      <span class="brand__square"></span>
      <span class="brand__name">Veltrano Energy</span>
    </div>
  </section>

  <section class="card card--back">
    <div class="brand">
      <span class="brand__square"></span>
      <span class="brand__name">Veltrano Energy</span>
    </div>

    <div class="offices">
      <p class="offices__label">office</p>
      <div class="offices__flags">
        <span class="offices__flag offices__flag--a" role="img" aria-label="United States flag"></span>
        <span class="offices__flag offices__flag--b" role="img" aria-label="Canada flag"></span>
        <span class="offices__flag offices__flag--c" role="img" aria-label="United Kingdom flag"></span>
      </div>
    </div>

    <div class="divider"></div>

    <div class="person">
      <h1 class="person__name">Dorian Kettle</h1>
      <p class="person__title">Founder / Operations Strategist</p>
    </div>

    <div class="contact contact--address">
      <svg class="contact__icon" width="30" height="34" viewBox="0 0 30 34" fill="none" stroke="var(--cyan)" stroke-width="2">
        <path d="M15 26 C9 19 6 15 6 11 a9 9 0 0 1 18 0 c0 4 -3 8 -9 15z"/>
        <circle cx="15" cy="11" r="3.5"/>
        <path d="M10 23 C4 24 2 26 2 28 c0 3 6 5 13 5 s13-2 13-5 c0-2-2-4-8-5"/>
      </svg>
      <p class="contact__text">Veltrano Energy<br>4821 Harbor Crest Lane<br>Marlow Bay, FL 30417<br>555.014.2286</p>
    </div>

    <div class="contact contact--web">
      <svg class="contact__icon" width="30" height="21" viewBox="0 0 30 21" fill="none" stroke="var(--cyan)" stroke-width="2">
        <rect x="1" y="1" width="28" height="19"/>
        <path d="M1 1 L15 12 L29 1 M1 20 L11 9 M29 20 L19 9"/>
      </svg>
      <p class="contact__text">www.veltranoenergy.example</p>
    </div>

    <div class="tagline">No debt, no liens, no maintenance, just savings.</div>
  </section>

</body>
</html>
```